Flip top bottle and neck label

Bottle label - combo set

Main + neck concept

Because kombucha is considered to be the actual fountain of youth considering all of it's beneficial properties for the body. It is the fullest system ''tonic'' you can find. kombucha is associated with, health, awakening, simplicity, perseverance, young yet wise. NOTHING is added, the sweetness comes from the dried fruits

Classic / Vintage / Mono(Duo)Tone / Simple / Distressed / Exquisite / Refined / Hand-Made / Timeless / Everlasting

This brand is mysterious, This is a brand that appears to be ancient medicine... it is ancient medicine...
This is a brand label that will look harmless if a kid sees it. Kids will ignore it.
This brand will look "interesting" if an adult sees it. Adults will remember seeing it.
This brand has an "old world feel", and Wild west "cure all"
It will remind them a bit of 70's Rock posters - you had to be "on something" to 'understand' or 'get' them
The Label has the look of vintage perfume bottles and their perfect combination of glass and metal materials
Icons can include: French Canadian (fleur de lis), family business, Quebec

It would be cool to have area on the labels for handwriting things like: date / flavour / fermentation period / notes
flavor ___________
ingredients ___________
fermentation time ___________
notes ___________

To accomplish this brand look - we'll need multiple fonts - some with serifs and calligraphy - some that are hard and bold. We'll need to incorporate typesetting on curves and unique lines to create drama in the label. You want viewers to be drawn into the detail and complexity of the simple distressed - perfectly balanced - vintage looking label.

Colour concepts:
dark label or dark text on a white label, with gold or silver ornaments

OR

Monotone + one colour for the flavor
Each label is say dark text, and has a single colour splash text and some detail to denote it's say cherry
This can look like a series (red cherry, orange for peach, purple for plum)

++++++++++

This text MUST appear somewhere:

Marcel's Kombucha
marcelskombucha.example

This text COULD appear - but not required:

Naturally carbonated keep cool, do not shake.
May contain trace elements of alcohol 0.5%.
Keep cool at all times, handle with care.
Naturally carbonated.
Fine teas, fine kombucha.
Homemade, naturally carbonated in the bottle.
Fermentation: 15 to 21 days.
Since 2012.
Ingredients: spring water, organic kombucha culture, organic sugar (no sugar added), fruit juices.
Expiration date (probably on removable stickers to keep the logo intact and standard)
Flavor (maybe a fruit logo)
Updates

I know there was a 48 hr limit on this design - just posting a note that this 48 period isn't a "hard drop deadline". We are open to flexibility in the delivery, we appreciate all the hard work and speed - and understand 48 hrs is a very short time period. Please understand this was our attempt at a beginning guideline. Thanks and again we appreciate you efforts!

Reason: Love the submissions - would love to see even more concepts!

Target Market(s)

Healthy Adults
Intelligent
Aware
Forward Thinking
Target market is those who understand holistic medicine and understand natural paths to health

Industry/Entity Type

Health And Wellness

Font styles to use
Serif
Sans Serif
Decorative
Script

Requirements
Must have
• Marcel's Kombucha
• marcelskombucha.example
• In text on the label for both the body of the bottle and the neck of the bottle
Nice to have
• Naturally carbonated keep cool, do not shake.
• May contain trace elements of alcohol 0.5%.
• Keep cool at all times, handle with care.
• Naturally carbonated.
• Fine teas, fine kombucha.
• Homemade, naturally carbonated in the bottle.
• Fermentation: 15 to 21 days.
• Since 2012.
• Ingredients: spring water, organic kombucha culture, organic sugar (no sugar added), fruit juices.
• Expiration date (probably on removable stickers to keep the logo intact and standard)
• Flavor (maybe a fruit logo)
Should not have
• multiple colours
• rainbows of colour
• photographic images (stylized images and icons are fine)

```html
<!DOCTYPE html>
<html lang="en">
<head>
<meta charset="utf-8">
<title>Marcel's Kombucha – Neck Label</title>
<link href="https://fonts.googleapis.com/css2?family=Libre+Caslon+Text&display=swap" rel="stylesheet">
<style>
  :root {
    --label-black: #000000;
    --gold-light: #e6d7a8;
    --gold-mid: #b9a678;
    --gold-dark: #5e5236;
    --gold-text: #b5a17a;
    --frame-shadow: #3b3527;
  }
  html, body {
    margin: 0;
    padding: 0;
    width: 1200px;
    height: 200px;
    overflow: hidden;
    background: #ffffff;
  }
  .neck-label {
    position: relative;
    width: 1200px;
    height: 200px;
    box-sizing: border-box;
    background: var(--label-black);
    border: 3px solid var(--gold-mid);
    border-radius: 8px;
    box-shadow: inset 0 0 0 2px var(--frame-shadow);
    overflow: hidden;
  }
  .neck-label__end {
    position: absolute;
    top: 0;
    bottom: 0;
    width: 90px;
  }
  .neck-label__end--left {
    left: 0;
    background: linear-gradient(to right,
      var(--gold-dark) 0%,
      var(--gold-light) 28%,
      var(--gold-mid) 50%,
      rgba(0,0,0,0) 100%);
  }
  .neck-label__end--right {
    right: 0;
    background: linear-gradient(to left,
      var(--gold-dark) 0%,
      var(--gold-light) 28%,
      var(--gold-mid) 50%,
      rgba(0,0,0,0) 100%);
  }
  .neck-label__rule {
    position: absolute;
    left: 0;
    right: 0;
    height: 3px;
    background: linear-gradient(to right, var(--gold-dark), var(--gold-light) 20%, var(--gold-mid) 50%, var(--gold-light) 80%, var(--gold-dark));
  }
  .neck-label__rule--top { top: 0; }
  .neck-label__rule--bottom { bottom: 0; }
  .brand-name {
    position: absolute;
    top: 97px;
    transform: translate(-50%, -50%);
    margin: 0;
    white-space: nowrap;
    font-family: "Libre Caslon Text", Georgia, serif;
    font-size: 32px;
    font-weight: 400;
    line-height: 1;
    color: var(--gold-text);
  }
  .brand-name--one { left: 252px; }
  .brand-name--two { left: 600px; }
  .brand-name--three { left: 948px; }
</style>
</head>
<body>
  <div class="neck-label">
    <div class="neck-label__end neck-label__end--left"></div>
    <div class="neck-label__end neck-label__end--right"></div>
    <div class="neck-label__rule neck-label__rule--top"></div>
    <div class="neck-label__rule neck-label__rule--bottom"></div>

    <p class="brand-name brand-name--one">Marcel's Kombucha</p>
    <p class="brand-name brand-name--two">Marcel's Kombucha</p>
    <p class="brand-name brand-name--three">Marcel's Kombucha</p>
  </div>
</body>
</html>
```